6" x 11" Print Mailer selling Fiber Internet Services

We need to design a 6" x 11" mailer offering Fiber Internet Services. People receiving this mailer are targeted specifically because fiber has been deployed in their neighborhoods and they can now sign up for fiber service to their door.

We want to lead with "Fiber is now at your door" to hammer home the fact that they can have fiber internet. The picture on the front should be a colorful set of fiber optic cables, the back side can be a happy family using a laptop or some device

We want to advertise two plans:

1) 250 Mbps for $34.95/mo
2) 1 Gbps for $46.95/mo

We need a small but obvious disclaimer that says "Plus $30 Meridel fees"

We want to offer a free month of service for signing up when they mention this mailer and to advertise our 24/7 Technical Support and No Long Term Commitments

We want our Logo (attached) phone number and website visible clearly on the front and back

555-372-9046
www.brovanet.example

Target Market(s)

Residential Households that have fiber internet services now available

Industry/Entity Type

Internet Service Provider

Font styles to use
Serif
Sans Serif
Other font styles liked:
• Futurona is the name of the font in our logo

Requirements
Must have
• Room for the NPDS to print the postage and address on the back. You can use this link for specific requirements from npds: https://about.npds-example.org/guides/g412/g412_003.htm
Nice to have
• Base the color scheme around our logo colors. This can be a vertical or horizontal (or vertical one side, horizontal on the other)
Should not have
• Do not replicate the mailer I have attached, we want something new - it is there for reference.

```html
<!DOCTYPE html>
<html lang="en">
<head>
<meta charset="utf-8">
<title>Brovanet Fiber Mailer</title>
<link rel="stylesheet" href="https://fonts.googleapis.com/css2?family=Oswald:wght@700&family=Montserrat:wght@400;500;700&family=Roboto+Condensed:wght@500&display=swap">
<style>
  :root{
    --page:#dcdcdc;
    --shadow:#c7c7c7;
    --white:#ffffff;
    --brand:#2f8fd8;
    --brand-deep:#1f4fc4;
    --navy:#0b1a45;
    --headline-bg:#8cbbe7;
    --plan-band:#2386cf;
    --note-band:#cde3f2;
    --body-text:#3d4a57;
    --ink:#1b2530;
  }
  *{box-sizing:border-box;margin:0;padding:0}
  html,body{width:1200px;height:2207px;overflow:hidden}
  body{background:var(--page);position:relative;font-family:"Montserrat",sans-serif}

  .card-shadow{position:absolute;width:1000px;height:545px;background:var(--shadow)}
  .card{position:absolute;width:1000px;height:545px;background:var(--white);overflow:hidden}

  /* FRONT */
  .front{left:150px;top:380px}
  .front-shadow{left:105px;top:440px}
  .hero-photo{position:absolute;inset:0;
    background:
      radial-gradient(ellipse 30% 40% at 68% 42%, rgba(120,220,255,.55), transparent 70%),
      radial-gradient(ellipse 60% 50% at 40% 55%, #2a5fd6, transparent 80%),
      linear-gradient(120deg,#1f55c9 0%,#173a9e 45%,#0d1f5e 100%);}
  .front-frame{position:absolute;inset:0}
  .front .logo{position:absolute;left:52px;top:28px}
  .headline{position:absolute;left:0;top:236px;font-family:"Oswald",sans-serif;font-weight:700;color:var(--navy);text-transform:uppercase}
  .headline span{display:block;background:var(--headline-bg);padding:0 26px 0 36px;font-size:72px;line-height:76px;width:max-content;letter-spacing:-.5px}
  .headline span + span{margin-top:2px}
  .front-contact{position:absolute;top:468px;left:528px;display:flex;gap:46px;font-family:"Roboto Condensed",sans-serif;font-weight:500;font-size:21px;color:var(--ink)}
  .contact-item{display:flex;align-items:center;gap:10px}

  .logo{display:flex;align-items:center;gap:10px;color:var(--brand);font-family:"Montserrat",sans-serif;font-weight:400}
  .logo-dot{border-radius:50%;background:var(--brand)}
  .front .logo-name{font-size:50px;letter-spacing:-1px}
  .front .logo-dot{width:26px;height:26px}

  /* BACK */
  .back{left:150px;top:1320px}
  .back-shadow{left:105px;top:1380px}
  .offer-panel{position:absolute;left:0;top:0;width:465px;height:545px}
  .family-photo{height:222px;background:linear-gradient(180deg,#e9e4dc 0%,#d4cbbd 50%,#a8a4a0 100%)}
  .plans{height:136px;background:var(--plan-band);padding:20px 29px 0;color:var(--white)}
  .plan-row{display:flex;gap:10px}
  .plan{width:196px;height:78px;border:1px dashed rgba(255,255,255,.8);display:flex;flex-direction:column;justify-content:center;align-items:center;font-weight:700;font-size:21px;line-height:25px}
  .fees{text-align:center;font-size:13px;margin-top:10px}
  .fees b{font-weight:700}
  .perks{height:102px;background:var(--note-band);padding:22px 38px 0;color:var(--body-text);font-size:15px;line-height:18px}
  .perks b{font-weight:700}
  .back-footer{position:absolute;left:40px;top:472px;display:flex;align-items:center;font-size:11px;font-weight:700;color:var(--ink)}
  .back .logo-name{font-size:26px;letter-spacing:-.5px}
  .back .logo-dot{width:14px;height:14px}
  .back .logo{gap:6px}
  .divider{width:1px;height:40px;background:#8b96a3;margin:0 22px 0 20px}
  .back-footer .contact-item{gap:6px;margin-right:26px}
</style>
</head>
<body>

<div class="card-shadow front-shadow"></div>
<section class="card front">
  <div class="hero-photo" role="img" aria-label="Colorful glowing fiber optic cable strands against a deep blue background"></div>
  <svg class="front-frame" width="1000" height="545" viewBox="0 0 1000 545">
    <polygon points="0,0 415,0 376,107 0,107" fill="#fff"/>
    <polygon points="460,0 500,0 461,107 421,107" fill="var(--brand-deep)"/>
    <polygon points="512,0 548,0 509,107 473,107" fill="#fff"/>
    <polygon points="548,0 1000,0 1000,0 548,0" fill="none"/>
    <polygon points="475,443 1000,443 1000,545 430,545" fill="#fff"/>
    <polygon points="360,443 388,443 345,545 317,545" fill="#fff"/>
    <polygon points="418,443 446,443 403,545 375,545" fill="#fff"/>
  </svg>
  <div class="logo"><span class="logo-dot"></span><span class="logo-name">Brovanet</span></div>
  <h1 class="headline"><span>Fiber is</span><span>Now at your door</span></h1>
  <div class="front-contact">
    <div class="contact-item">
      <svg width="20" height="20" viewBox="0 0 24 24"><path d="M6.6 10.8a15 15 0 0 0 6.6 6.6l2.2-2.2c.3-.3.7-.4 1-.2 1.1.4 2.3.6 3.6.6.6 0 1 .4 1 1V20c0 .6-.4 1-1 1A17 17 0 0 1 3 4c0-.6.4-1 1-1h3.5c.6 0 1 .4 1 1 0 1.3.2 2.5.6 3.6.1.3 0 .7-.2 1z" fill="var(--brand)"/></svg>
      <span>555-372-9046</span>
    </div>
    <div class="contact-item">
      <svg width="20" height="20" viewBox="0 0 24 24" fill="none" stroke="var(--brand)" stroke-width="2"><circle cx="12" cy="12" r="9"/><path d="M3 12h18M12 3c3 3 3 15 0 18M12 3c-3 3-3 15 0 18"/></svg>
      <span>www.brovanet.example</span>
    </div>
  </div>
</section>

<div class="card-shadow back-shadow"></div>
<section class="card back">
  <div class="offer-panel">
    <div class="family-photo" role="img" aria-label="Happy family sitting together on a sofa using a laptop in a bright living room"></div>
    <div class="plans">
      <div class="plan-row">
        <div class="plan"><span>250 Mbps</span><span>for $34.95/mo</span></div>
        <div class="plan"><span>1 Gbps</span><span>for $46.95/mo</span></div>
      </div>
      <p class="fees">*** Plus <b>$30</b> Meridel fees***</p>
    </div>
    <div class="perks">
      <p>We want to offer a free month of service for signing up when they mention this mailer and to advertise our <b>24/7</b> Technical Support and No Long Term Commitments</p>
    </div>
  </div>
  <div class="back-footer">
    <div class="logo"><span class="logo-dot"></span><span class="logo-name">Brovanet</span></div>
    <span class="divider"></span>
    <div class="contact-item">
      <svg width="11" height="11" viewBox="0 0 24 24"><path d="M6.6 10.8a15 15 0 0 0 6.6 6.6l2.2-2.2c.3-.3.7-.4 1-.2 1.1.4 2.3.6 3.6.6.6 0 1 .4 1 1V20c0 .6-.4 1-1 1A17 17 0 0 1 3 4c0-.6.4-1 1-1h3.5c.6 0 1 .4 1 1 0 1.3.2 2.5.6 3.6.1.3 0 .7-.2 1z" fill="var(--brand)"/></svg>
      <span>555-372-9046</span>
    </div>
    <div class="contact-item">
      <svg width="11" height="11" viewBox="0 0 24 24" fill="none" stroke="var(--brand)" stroke-width="2.4"><circle cx="12" cy="12" r="9"/><path d="M3 12h18M12 3c3 3 3 15 0 18M12 3c-3 3-3 15 0 18"/></svg>
      <span>www.brovanet.example</span>
    </div>
  </div>
</section>

</body>
</html>
```